German Auto Restoration Website Design

We are working with a Classic Car Restoration company in California.
They compete with guys like this:
https://torvexautorestoration.com

We could not find any auto restoration company websites for inspiration. We attached some images of the type of work they do.

Thank you for taking the time to consider designing a website for us. We are web developers based in Stockton, CA, USA. Most of our projects go through the same process. Understanding this process may help you win a project with us. We custom-code all of our websites in-house. We don’t have any requirements as to what tools you use for your design, but we ask that you follow these guidelines.

IMAGES:
If you use any images or icons in the design, we ask that you have a link to the asset so we can purchase the image/icon. Most of the designs we submit do not have the customer’s images on them unless they have some great images. Be creative; show us the feeling you are trying to portray with your image choices. Use any royalty-free site you choose. We subscribe to Qinto and mainly use their images, but we can purchase images outside of Qinto. PLEASE NOTE: we will not submit designs to clients with watermarks on the images.

FONTS:
We ask that you identify the fonts you’re using in the design. This can be done in a message if you want. We typically use Plexa Fonts and Qinto Fonts.

CONTENT:
We're always open to different content and ideas. We often submit designs with stock images so the client can see our vision. We typically take pictures after the website launch to use their images with our vision. Lorem Ipsum is fine for paragraphs, but we ask that you make the Headers with correct English. We want to be able to show the vision and identify the sections of the website.

INSPIRATION:
We typically add a couple of links in the brief of websites we like to help you get started in your design.

REVISIONS:
We do not often ask for revisions of the designs unless we see something in the design that may not appeal to the client. If there are slight changes that we want to make, we do that in the development process.

FEEDBACK:
We rarely give feedback on designs during the design process. We are working on many website projects and do not have the time to provide feedback. We usually respond if your request is well thought out and asks specific questions, but a note asking “feedback, please” usually goes unanswered.

```html
<!DOCTYPE html>
<html lang="en">
<head>
<meta charset="utf-8">
<title>Veldhaus Restorations</title>
<link href="https://fonts.googleapis.com/css2?family=Roboto:wght@400;500;700&family=Roboto+Condensed:wght@400;500&display=swap" rel="stylesheet">
<style>
:root{
  --red:#e8202a;
  --yellow:#fff200;
  --ink:#1a1a1a;
  --grey:#6b6b6b;
  --dark:#1f1f1f;
  --white:#fff;
}
*{margin:0;padding:0;box-sizing:border-box}
html,body{width:1200px;height:4206px;overflow:hidden}
body{position:relative;background:var(--white);font-family:'Roboto',sans-serif;color:var(--ink)}
.abs{position:absolute}
.head{font-family:'Roboto Condensed',sans-serif;font-weight:400;text-transform:uppercase}
.photo{position:absolute}
.site-header{position:absolute;left:0;top:0;width:1200px;height:116px;background:#fff}
.brand{position:absolute;left:60px;top:38px;display:flex;align-items:center;gap:12px;font-size:19px;letter-spacing:5px;font-weight:500;color:var(--ink)}
.brand-dot{width:16px;height:16px;background:var(--red)}
.search{position:absolute;left:568px;top:20px;width:281px;height:40px;border:1px solid #ddd;border-radius:20px;background:#f4f4f4;font-size:12px;color:#999;padding:11px 24px}
.search-btn{position:absolute;right:-1px;top:-1px;width:42px;height:40px;background:var(--red);border-radius:0 20px 20px 0;display:flex;align-items:center;justify-content:center}
.call-icon{position:absolute;left:895px;top:22px;width:34px;height:34px;border-radius:50%;background:#f2e600;display:flex;align-items:center;justify-content:center}
.call-label{position:absolute;left:944px;top:16px;font-size:12px;color:#888}
.call-number{position:absolute;left:944px;top:37px;font-size:17px;font-weight:700}
.nav{position:absolute;top:82px;left:0;font-size:14px;font-weight:500}
.nav span{position:absolute;white-space:nowrap}
.nav .active{color:var(--red)}
.hero{position:absolute;left:0;top:116px;width:1200px;height:607px;background:radial-gradient(ellipse at 10% 10%,#7a4a1a 0%,#2a1a0e 30%,#0b0b0b 60%,#050505 100%)}
.hero-car{left:645px;top:178px;width:433px;height:335px;border-radius:40px 40px 20px 20px;background:linear-gradient(180deg,#cfd2d6 0%,#8f9398 40%,#b3242b 70%,#3a0c0e 100%)}
.hero-kicker{left:111px;top:176px;font-size:30px;color:#fff}
.hero-title{left:111px;top:224px;font-size:43px;color:#fff}
.hero-text{left:111px;top:290px;width:500px;font-size:16px;line-height:26px;color:#fff;font-weight:500}
.btn{position:absolute;background:var(--yellow);border-radius:25px;font-weight:700;font-size:16px;color:var(--ink);display:flex;align-items:center;justify-content:center;gap:8px}
.btn-arrow{width:14px;height:14px;border-radius:50%;background:var(--ink);display:inline-flex;align-items:center;justify-content:center}
.sec-title{position:absolute;left:0;width:1200px;text-align:center;font-size:34px}
.bar{position:absolute;left:566px;width:68px;height:4px;background:var(--red);border-radius:2px}
.sec-text{position:absolute;left:180px;width:840px;text-align:center;font-size:15px;line-height:24px;color:var(--grey)}
.card{position:absolute;top:973px;width:305px;height:278px;overflow:hidden}
.card-caption{position:absolute;left:36px;bottom:26px;color:#fff;font-weight:700;font-size:18px}
.about-photo{left:0;top:1344px;width:599px;height:607px;background:linear-gradient(160deg,#8fb3d8 0%,#5c7a4a 35%,#d9d9d4 55%,#6e6a64 100%)}
.about-panel{position:absolute;left:599px;top:1344px;width:601px;height:607px;background:var(--red)}
.about-title{left:673px;top:1414px;font-size:36px;color:#fff}
.about-text{left:673px;top:1488px;width:488px;font-family:'Roboto Condensed',sans-serif;font-size:16.5px;line-height:29.7px;color:#fff;text-align:justify}
.video{left:111px;top:2181px;width:977px;height:495px;border-radius:16px;background:linear-gradient(180deg,#6f7a6a 0%,#3d4c44 35%,#22364e 60%,#4a4b4e 100%)}
.play{position:absolute;left:554px;top:2382px}
.newsletter{position:absolute;left:0;top:2763px;width:1200px;height:313px;background:linear-gradient(90deg,#d91c24,#ec2f35 50%,#d91c24)}
.nl-title{left:0;top:2808px;width:1200px;text-align:center;font-size:36px;color:#fff;font-weight:500}
.nl-text{left:180px;top:2892px;width:840px;text-align:center;font-size:15px;line-height:24px;color:#fff}
.field{position:absolute;top:2970px;width:286px;height:41px;border-radius:21px;background:#fff;font-size:13px;color:#555;padding:13px 22px}
.g{position:absolute;width:302px;height:228px}
.footer{position:absolute;left:0;top:3806px;width:1200px;height:400px;background:var(--dark);color:#fff}
.f-brand{left:111px;top:3878px;display:flex;align-items:center;gap:10px;font-size:15px;letter-spacing:4px;color:#fff;font-weight:500}
.f-text{left:111px;top:3938px;width:270px;font-size:13px;line-height:19px;color:#eee}
.social{position:absolute;top:4014px;width:28px;height:28px;border:1.5px solid #fff;border-radius:50%}
.f-head{position:absolute;top:3870px;font-size:19px;font-weight:500}
.f-list{position:absolute;top:3918px;list-style:none;font-size:14px;line-height:33px}
.f-list li::before{content:"»";color:var(--yellow);margin-right:14px}
.f-contact{position:absolute;left:867px;top:3918px;font-size:14px;line-height:21px}
.f-contact .row{display:flex;gap:16px;margin-bottom:12px}
.f-contact .ico{width:14px;color:var(--yellow);flex:none}
.rule{position:absolute;left:111px;top:4131px;width:978px;height:1px;background:#3a3a3a}
.copy{position:absolute;left:0;top:4166px;width:1200px;text-align:center;font-size:13px;color:#eee}
</style>
</head>
<body>

<header class="site-header">
  <div class="brand"><span class="brand-dot"></span>VELDHAUS RESTORATIONS</div>
  <div class="search">Search...
    <div class="search-btn"><svg width="14" height="14" viewBox="0 0 14 14"><circle cx="6" cy="6" r="4.2" fill="none" stroke="#fff" stroke-width="2"/><line x1="9" y1="9" x2="12.5" y2="12.5" stroke="#fff" stroke-width="2"/></svg></div>
  </div>
  <div class="call-icon"><svg width="16" height="16" viewBox="0 0 24 24"><path d="M6.6 10.8a15 15 0 0 0 6.6 6.6l2.2-2.2c.3-.3.7-.4 1-.2 1.1.4 2.3.6 3.6.6.6 0 1 .4 1 1V20c0 .6-.4 1-1 1A17 17 0 0 1 3 4c0-.6.4-1 1-1h3.5c.6 0 1 .4 1 1 0 1.3.2 2.5.6 3.6.1.3 0 .7-.2 1z" fill="#222"/></svg></div>
  <div class="call-label">Call Us Today</div>
  <div class="call-number">+1 555 014 2290</div>
  <nav class="nav">
    <span class="active" style="left:462px">HOME</span>
    <span style="left:540px">ABOUT</span>
    <span style="left:625px">RESTORATION SERVICES</span>
    <span style="left:834px">PORTFOLIO</span>
    <span style="left:950px">BLOG</span>
    <span style="left:1024px">CONTACT</span>
  </nav>
</header>

<section class="hero" role="img" aria-label="Dark garage interior with warm window light">
  <div class="photo hero-car" role="img" aria-label="Rear view of a classic sports car in striped racing colours"></div>
  <div class="abs head hero-kicker">Welcome to</div>
  <h1 class="abs head hero-title">Veldhaus Restorations</h1>
  <p class="abs hero-text">Lorem ipsum dolor sit amet, consectetur adipiscing elit, sed do eiusmod tempor incididunt ut labore et dolore magna aliqua.</p>
  <a class="btn" style="left:111px;top:374px;width:204px;height:49px">CONTACT US <span class="btn-arrow"><svg width="8" height="8" viewBox="0 0 8 8"><path d="M2 1l4 3-4 3z" fill="#fff200"/></svg></span></a>
</section>

<h2 class="head sec-title" style="top:800px">Our Services</h2>
<div class="bar" style="top:847px"></div>
<p class="sec-text" style="top:868px">Lorem ipsum dolor sit amet, consectetur adipiscing elit, sed do eiusmod tempor incididunt ut labore et dolore magna aliqua. Ut enim ad minim veniam, quis nostrud exercitation ullamco laboris commodo consequat</p>

<div class="card" style="left:111px;background:linear-gradient(135deg,#b3121a 0%,#3a3a3c 35%,#1c1c1e 70%,#555 100%)" role="img" aria-label="Close-up of a sports car wheel and red brake caliper"><div class="card-caption">Lorem ipsum dolor sit amet</div></div>
<div class="card" style="left:442px;background:linear-gradient(180deg,#9dbb52 0%,#c9c4a6 45%,#7b7a66 75%,#4f6a2c 100%)" role="img" aria-label="Classic coupe parked on grass"><div class="card-caption">Lorem ipsum dolor sit amet</div></div>
<div class="card" style="left:772px;background:linear-gradient(160deg,#2a2c30 0%,#0e0f11 50%,#3b3d42 100%)" role="img" aria-label="Car key resting on a leather surface"><div class="card-caption">Lorem ipsum dolor sit amet</div></div>

<div class="photo about-photo" role="img" aria-label="Restored white rounded vintage car on cobblestones"></div>
<div class="about-panel"></div>
<h2 class="abs head about-title">About Us</h2>
<div class="abs" style="left:673px;top:1463px;width:68px;height:4px;background:var(--yellow);border-radius:2px"></div>
<p class="abs about-text">Lorem ipsum dolor sit amet, consectetur adipiscing elit, sed do eiusmod tempor incididunt ut labore et dolore magna aliqua. Ut enim ad minim veniam, quis nostrud exercitation ullamco laboris nisi ut aliquip ex ea commodo consequat. Duis aute irure dolor in reprehenderit in voluptate velit esse cillum dolore eu fugiat nulla pariatur. Excepteur sint occaecat cupidatat non proident, sunt in culpa qui officia deserunt mollit anim id est laborum.Lorem ipsum dolor sit amet, consectetur adipiscing elit, sed do eiusmod tempor incididunt ut labore et dolore magna aliqua. Ut enim ad minim veniam, quis nostrud exercitation ullamco laboris nisi ut aliquip ex ea commodo consequat Duis aute irure dolor.</p>
<a class="btn" style="left:673px;top:1821px;width:203px;height:49px">LEARN MORE <span class="btn-arrow"><svg width="8" height="8" viewBox="0 0 8 8"><path d="M2 1l4 3-4 3z" fill="#fff200"/></svg></span></a>

<h2 class="head sec-title" style="top:2028px">Our Videos</h2>
<div class="bar" style="top:2075px"></div>
<p class="sec-text" style="top:2096px">Lorem ipsum dolor sit amet, consectetur adipiscing elit, sed do eiusmod tempor incididunt ut labore et dolore magna aliqua. Ut enim ad minim veniam, quis nostrud exercitation ullamco laboris commodo consequat</p>
<div class="photo video" role="img" aria-label="Dark blue classic coupe parked in front of a glass building"></div>
<svg class="play" width="92" height="92" viewBox="0 0 92 92"><circle cx="46" cy="46" r="46" fill="rgba(255,255,255,.8)"/><circle cx="46" cy="46" r="25" fill="none" stroke="#111" stroke-width="5"/><path d="M39 34l17 12-17 12z" fill="#111"/></svg>

<section class="newsletter" role="img" aria-label="Red tinted close-up of a classic car"></section>
<h2 class="abs head nl-title">Subscribe to our Newsletter</h2>
<div class="abs" style="left:566px;top:2864px;width:68px;height:4px;background:var(--yellow);border-radius:2px"></div>
<p class="abs nl-text">Lorem ipsum dolor sit amet, consectetur adipiscing elit, sed do eiusmod tempor incididunt ut labore et dolore magna aliqua. Ut enim ad minim veniam, quis nostrud exercitation ullamco laboris commodo consequat</p>
<div class="field" style="left:214px">Enter Your Name</div>
<div class="field" style="left:514px">Enter Email Address</div>
<a class="btn" style="left:813px;top:2970px;width:172px;height:41px">SUBMIT NOW</a>

<h2 class="head sec-title" style="top:3157px">Our Gallery</h2>
<div class="bar" style="top:3204px"></div>
<div class="g" style="left:129px;top:3240px;background:linear-gradient(180deg,#4d7a3a,#e07a1e 55%,#5c8a2c)" role="img" aria-label="Orange classic sports car on grass"></div>
<div class="g" style="left:451px;top:3240px;background:linear-gradient(180deg,#4e7a44,#d9d6cc 60%,#8a8a7a)" role="img" aria-label="White rounded vintage car on a country road"></div>
<div class="g" style="left:769px;top:3240px;background:linear-gradient(160deg,#2d5b62,#b7bdbf 50%,#3a3e42)" role="img" aria-label="Wheel arch of a teal classic car"></div>
<div class="g" style="left:129px;top:3490px;background:linear-gradient(150deg,#3d6a8e,#d9d9d4 55%,#2e4a66)" role="img" aria-label="Headlight of a blue vintage car"></div>
<div class="g" style="left:451px;top:3490px;background:linear-gradient(150deg,#8a8a86,#e8e6e0 55%,#5a5a56)" role="img" aria-label="Chrome grille and headlight of a white classic saloon"></div>
<div class="g" style="left:769px;top:3490px;background:linear-gradient(170deg,#9aa0a6,#c9ccce 50%,#2f5d9e)" role="img" aria-label="Silver vintage coupe front bumper"></div>

<footer class="footer"></footer>
<div class="abs f-brand"><span class="brand-dot"></span>VELDHAUS RESTORATIONS</div>
<p class="abs f-text">Lorem ipsum dolor consectetur adipiscing elit, sed do eiusmod tempor incididunt ut labore et dolore magna aliqua.</p>
<span class="social" style="left:112px"></span>
<span class="social" style="left:143px"></span>
<span class="social" style="left:175px"></span>
<span class="social" style="left:208px"></span>

<div class="f-head" style="left:455px;color:#fff">Company</div>
<ul class="f-list" style="left:455px;color:#fff">
  <li>Home</li><li>About</li><li>Restoration Services</li><li>Portfolio</li><li>Blog</li><li>Contact</li>
</ul>
<div class="f-head" style="left:681px;color:#fff">Resources</div>
<ul class="f-list" style="left:681px;color:#fff">
  <li>Blog</li><li>Reliability</li><li>Terms of Use</li><li>Privacy</li><li>Contact Us</li>
</ul>
<div class="f-head" style="left:867px;color:#fff">Contact us</div>
<div class="f-contact" style="color:#fff">
  <div class="row"><svg class="ico" width="14" height="18" viewBox="0 0 14 18"><path d="M7 0a6 6 0 0 0-6 6c0 4.5 6 12 6 12s6-7.5 6-12a6 6 0 0 0-6-6zm0 8.5A2.5 2.5 0 1 1 7 3.5a2.5 2.5 0 0 1 0 5z" fill="#fff200"/></svg><span>45,Lorem ipsum dolor sit<br>adipiscing eiusmounted.</span></div>
  <div class="row"><svg class="ico" width="14" height="16" viewBox="0 0 14 16"><rect x="3" y="1" width="8" height="14" rx="1.5" fill="none" stroke="#fff200" stroke-width="1.6"/></svg><span>+1 555 014 2290</span></div>
  <div class="row"><svg class="ico" width="14" height="16" viewBox="0 0 14 16"><rect x="1" y="3" width="12" height="11" rx="1.5" fill="#fff200"/></svg><span>0123 555 0147</span></div>
  <div class="row"><svg class="ico" width="14" height="14" viewBox="0 0 14 14"><rect x="1" y="2.5" width="12" height="9" fill="none" stroke="#fff200" stroke-width="1.4"/><path d="M1 3l6 5 6-5" fill="none" stroke="#fff200" stroke-width="1.4"/></svg><span>info@veldhausrestoration.com</span></div>
</div>
<div class="rule"></div>
<p class="copy">© 2023 Veldhaus Restoration &nbsp;|&nbsp; All Rights Reserved &nbsp; |</p>

</body>
</html>
```